Professional, Attractive, Simple Website Needed!!

We completed the design for our logo.

We need a website built out around this.

Here are a couple samples of how we want ours formatted.

http://brvntapower.com

http://www.halvorbeam.com/lp/free-quote?LeadSource=Search%20Engine&ProgramName=webquery&experience=qual&language=en&type=brd&gclid=Xq7RTPwmEYKDLAvUHbsNQkfPZrTcGwnJuoVbXeLqHmRYdAsWtPkMcNfBYgzTrUoQJhEdWvKpYaLsZbCmNDgQwTxAoKpXbT_qkR

http://morvalo.co

Reason: Extending this deadline due to our delay in providing designers with content for each page. This is coming in next 24 hours.

Reason: Due to scheduling conflicts and extended travel delays related to Puerto Rico, the deadline has been extended. Your patience is greatly appreciated.

Reason: Travel and scheduling conflicts have made it impossible to give this project the thorough review it deserves, therefore I am extending the deadline. Thank you for your patience!

Target Market(s)

Home Owners who earn 60k + household annually

Industry/Entity Type

It Professional

Coding

Coded - Design and coding required

Number of Pages Required

5+ page

Font styles to use
Serif

Colors
34a7d8
9bcb3c

Requirements
Must have
• Simple
• Lead form Entry (Ability for visitor to enter Name, number and address for a quote)
• Sleek Design
• Professional
• Testimonials
• Use color Scheme of Design Logo Attached
Nice to have
• Video when site starts
• Like this
• https://www.vidmarrow.com/watch?v=qT8mRpXw2Ka&feature=vidm.ro
Should not have
• Should not include Commercial solar
• Should not include wind power

```html
<!DOCTYPE html>
<html lang="en">
<head>
<meta charset="utf-8">
<title>Sunvale Energy</title>
<link href="https://fonts.googleapis.com/css2?family=Open+Sans:wght@400;600;700;800&display=swap" rel="stylesheet">
<style>
:root{
  --blue:#34a7d8;
  --blue-dark:#1f7fb8;
  --green:#9bcb3c;
  --green-dark:#86b42c;
  --ink:#333638;
  --muted:#7a7f84;
  --light:#f2f4f5;
  --footer:#2f3133;
  --footer-base:#252627;
  --white:#ffffff;
}
*{margin:0;padding:0;box-sizing:border-box}
html,body{width:1200px;height:2636px;overflow:hidden}
body{position:relative;font-family:"Open Sans",Arial,sans-serif;color:var(--ink);background:var(--white)}
.abs{position:absolute}

/* header */
.site-header{left:0;top:0;width:1200px;height:88px;background:var(--white);display:flex;align-items:center;justify-content:space-between;padding:0 40px 0 20px;box-shadow:0 1px 4px rgba(0,0,0,.08);z-index:5}
.brand{display:flex;align-items:center;gap:8px;font-weight:800;font-size:20px;color:var(--blue);letter-spacing:.5px}
.brand-dot{width:34px;height:34px;border-radius:50%;background:var(--green)}
.main-nav{display:flex;align-items:center;gap:34px;font-size:14px;color:var(--ink)}
.btn-quote{background:var(--blue);color:var(--white);font-weight:700;font-size:13px;padding:9px 14px;border-radius:2px}

/* hero */
.hero{left:0;top:88px;width:1200px;height:700px;background:linear-gradient(180deg,#1f2f45 0%,#3b4a5e 40%,#6b5c52 75%,#8a6b58 100%);clip-path:polygon(0 0,100% 0,100% 88%,50% 100%,0 88%)}
.hero-title{top:220px;width:1200px;text-align:center;color:var(--white);font-weight:700;font-size:62px;letter-spacing:1px}
.hero-sub{top:300px;width:1200px;text-align:center;color:var(--white);font-weight:700;font-size:19px;letter-spacing:.5px}
.video-frame{left:360px;top:400px;width:480px;height:340px;border:10px solid var(--green);background:linear-gradient(135deg,#5f6f78,#8f9aa0 50%,#6e7a70)}
.play{left:570px;top:540px;width:60px;height:60px}

/* about */
.section-title{width:1200px;text-align:center;font-weight:700;font-size:34px;color:var(--ink)}
.lead{left:170px;width:860px;text-align:center;font-size:13px;line-height:22px;color:var(--muted)}
.lead a{color:var(--blue);text-decoration:none}

/* lifestyle */
.lifestyle{left:0;top:1000px;width:1200px;height:660px;background:var(--light)}
.benefit{width:120px;height:120px;border-radius:50%;background:var(--green);border:6px solid #c8e394;display:flex;align-items:center;justify-content:center}
.benefit-label{width:200px;text-align:center;font-size:15px;font-weight:600;color:var(--ink)}

/* quote */
.quote-band{left:0;top:1600px;width:1200px;height:580px;background:linear-gradient(180deg,#3aa8dd 0%,var(--blue) 40%,var(--blue-dark) 100%);clip-path:polygon(0 10%,50% 0,100% 10%,100% 90%,50% 100%,0 90%)}
.quote-title{top:1745px;width:1200px;text-align:center;color:var(--white);font-weight:700;font-size:34px}
.quote-copy{left:170px;top:1810px;width:860px;text-align:center;color:#e6f4fb;font-size:13px;line-height:22px}
.lead-form{left:140px;top:1880px;width:920px;display:flex;gap:30px}
.field{flex:1;height:42px;background:var(--white);padding:0 12px;display:flex;align-items:center;font-size:13px;color:#999}
.btn-submit{left:516px;top:1960px;width:168px;height:42px;background:var(--green);color:var(--white);font-weight:700;font-size:13px;display:flex;align-items:center;justify-content:center}

/* testimonial */
.testimonial{left:230px;top:2196px;width:740px;text-align:center;font-size:13px;line-height:22px;color:var(--muted)}
.qmark{font-size:40px;line-height:40px;color:var(--blue);font-weight:800;top:2190px}
.client{left:0;top:2262px;width:1200px;display:flex;align-items:center;justify-content:center;gap:12px}
.client-dot{width:44px;height:44px;border-radius:50%;background:var(--blue)}
.client-name{font-weight:700;font-size:14px;color:var(--blue)}
.client-role{font-size:11px;color:var(--muted)}

/* footer */
.site-footer{left:0;top:2356px;width:1200px;height:244px;background:var(--footer);color:#cfd2d4}
.footer-col h4{color:var(--white);font-size:18px;font-weight:700;margin-bottom:14px}
.footer-col li{list-style:none;font-size:13px;line-height:28px}
.contact-row{display:flex;align-items:center;gap:10px;font-size:13px;line-height:18px;margin-bottom:12px}
.socials{display:grid;grid-template-columns:repeat(3,26px);gap:10px}
.social{width:26px;height:26px;border-radius:50%;background:#54585b}
.footer-brand{left:1020px;top:2390px;display:flex;align-items:center;gap:8px;font-weight:800;font-size:18px;color:var(--blue)}
.footer-base{left:0;top:2600px;width:1200px;height:36px;background:var(--footer-base);color:#8d9195;font-size:12px;display:flex;align-items:center;justify-content:center}
</style>
</head>
<body>

<header class="site-header abs">
  <div class="brand"><span class="brand-dot"></span>SUNVALE</div>
  <nav class="main-nav">
    <span>Home</span><span>Residential</span><span>Testimonials</span><span>Contact</span>
    <span class="btn-quote">GET A QUOTE</span>
  </nav>
</header>

<div class="hero abs" role="img" aria-label="Home roof covered in solar panels at dusk"></div>
<h1 class="hero-title abs">ENERGY SOLUTIONS</h1>
<p class="hero-sub abs">CONSECTETUER ADIPISCING ELIT, SED DIAM NONUMMY</p>
<div class="video-frame abs" role="img" aria-label="Intro video still showing a family beside solar panels"></div>
<svg class="play abs" viewBox="0 0 60 60"><circle cx="30" cy="30" r="27" fill="none" stroke="#9bcb3c" stroke-width="4"/><path d="M24 18 L42 30 L24 42 Z" fill="#9bcb3c"/></svg>

<h2 class="section-title abs" style="top:812px">SUNVALE ENERGY</h2>
<p class="lead abs" style="top:868px">Lorem ipsum dolor sit amet, consectetuer adipiscing elit, sed diam nonummy nibh euismod tincidunt ut laoreet dolore magna aliquam erat volutpat. Ut wisi enim ad minim veniam, quis nostrud exerci tation ullamcorper suscipit lobortis nisl ut aliquip ex ea <a>commodo consequat</a>. Duis autem vel eum iriure dolor in hendrerit in vulputate velit esse molestie consequat, vel illum dolore eu feugiat nulla facilisis at vero eros et accumsan et iusto odio dignissim qui blandit praesent luptatum zzril delenit augue duis dolore te feugait nulla facilisi. Nam liber tempor cum soluta nobis eleifend option congue nihil imperdiet doming id quod mazim placerat facer possim assum. <a>Read more</a></p>

<section class="lifestyle abs" aria-label="Improve your lifestyle"></section>
<h2 class="section-title abs" style="top:1040px">IMPROVE YOUR LIFESTYLE</h2>
<p class="lead abs" style="top:1098px">Lorem ipsum dolor sit amet, consectetuer adipiscing elit, sed diam nonummy nibh euismod tincidunt ut laoreet dolore magna aliquam erat volutpat. Ut wisi enim ad minim veniam, quis nostrud exerci tation ullamcorper suscipit lobortis nisl ut aliquip ex ea <a>commodo consequat</a>.</p>

<svg class="abs" style="left:150px;top:1220px" width="900" height="360" viewBox="0 0 900 360">
  <path d="M0 340 C200 320 420 200 620 110 C720 70 800 40 880 20" fill="none" stroke="#b8c2c8" stroke-width="2" stroke-dasharray="8 6"/>
  <path d="M868 14 L892 16 L876 32 Z" fill="#9bcb3c"/>
</svg>

<div class="benefit abs" style="left:232px;top:1460px">
  <svg width="56" height="56" viewBox="0 0 56 56" fill="none" stroke="#fff" stroke-width="5" stroke-linecap="round"><path d="M18 20 L28 8 L36 20"/><path d="M44 30 L46 44 L30 46"/><path d="M22 46 L8 40 L14 26"/></svg>
</div>
<p class="benefit-label abs" style="left:192px;top:1594px">Recycling</p>

<div class="benefit abs" style="left:532px;top:1360px">
  <svg width="56" height="56" viewBox="0 0 56 56"><path d="M10 46 C10 20 28 8 48 8 C48 30 36 46 10 46 Z" fill="#fff"/><path d="M12 44 L38 18" stroke="#9bcb3c" stroke-width="3"/></svg>
</div>
<p class="benefit-label abs" style="left:492px;top:1496px">Fossil Free Life</p>

<div class="benefit abs" style="left:828px;top:1262px">
  <svg width="56" height="56" viewBox="0 0 56 56"><path d="M32 4 L12 32 L26 32 L22 52 L44 22 L30 22 Z" fill="#fff"/></svg>
</div>
<p class="benefit-label abs" style="left:788px;top:1398px">Green Energy</p>

<section class="quote-band abs" role="img" aria-label="Rows of solar panels under a blue sky"></section>
<h2 class="quote-title abs">REQUEST A QUOTE</h2>
<p class="quote-copy abs">Lorem ipsum dolor sit amet, consectetuer adipiscing elit, sed diam nonummy nibh euismod tincidunt ut laoreet dolore magna aliquam erat volutpat. Ut wisi enim ad minim veniam, quis nostrud exerci tation ullamcorper.</p>
<form class="lead-form abs">
  <div class="field">Name</div>
  <div class="field">Contact No.</div>
  <div class="field">Address</div>
</form>
<div class="btn-submit abs">REQUEST A QUOTE</div>

<span class="qmark abs" style="left:196px">&ldquo;</span>
<p class="testimonial abs">Switching to solar was easier than we ever expected. The team walked us through every step, the panels went up in two days, and our monthly bills dropped right away. We would recommend them to any homeowner.</p>
<span class="qmark abs" style="left:984px">&rdquo;</span>
<div class="client abs">
  <span class="client-dot"></span>
  <div><div class="client-name">CLIENT NAME</div><div class="client-role">Homeowner, New York</div></div>
</div>

<footer class="site-footer abs">
  <div class="footer-col abs" style="left:110px;top:40px">
    <h4>NAVIGATION</h4>
    <ul><li>Home</li><li>Residential</li><li>Testimonials</li><li>Contact</li></ul>
  </div>
  <div class="footer-col abs" style="left:330px;top:40px;width:260px">
    <h4>CONTACT US</h4>
    <div class="contact-row"><svg width="16" height="20" viewBox="0 0 16 20"><path d="M8 0 C3.6 0 0 3.4 0 7.6 C0 13 8 20 8 20 C8 20 16 13 16 7.6 C16 3.4 12.4 0 8 0 Z" fill="#fff"/><circle cx="8" cy="7.5" r="3" fill="#2f3133"/></svg><span>214 Meadow Lane, Suite 12<br>Riverton, NY 14621</span></div>
    <div class="contact-row"><svg width="16" height="16" viewBox="0 0 16 16"><path d="M3 0 L6 4 L4 6 C5 8.5 7.5 11 10 12 L12 10 L16 13 L13 16 C6 15 1 10 0 3 Z" fill="#fff"/></svg><span>+1 555 014 2290</span></div>
    <div class="contact-row"><svg width="16" height="12" viewBox="0 0 16 12"><rect width="16" height="12" fill="#fff"/><path d="M0 0 L8 7 L16 0" fill="none" stroke="#2f3133" stroke-width="1.5"/></svg><span>hello@sunvale-energy.com</span></div>
  </div>
  <div class="footer-col abs" style="left:720px;top:40px">
    <h4>FOLLOW US</h4>
    <div class="socials"><span class="social"></span><span class="social"></span><span class="social"></span><span class="social"></span><span class="social"></span><span class="social"></span></div>
  </div>
</footer>
<div class="footer-brand abs"><span class="brand-dot" style="width:30px;height:30px"></span>SUNVALE</div>
<div class="footer-base abs">Copy Right &copy; 2017. All Right Reserved</div>

</body>
</html>
```